4 Page Pamphlet Guide Advertisement

Tidewind Bay Guide -

New publication starting, 5 businesses in Naha City,Okinawa and wants to make a brochure to highlight each and a front cover and a map on the back...

The expected size is (2) A4 size printed on both sides (4 designs) folded and stapled in the middle as a pamphlet. We've attached a sample photoshop file and we will provide additional photos and logos for content. Additionally you can get all other important content from each businesses' websites. SEE LAYOUT IN PHOTO SHOP FILE

www.barlanternok.com
www.velaloft.com
www.tavelostayinn.com
www.qrvlane.com
*Karaoke bar BLUE ECHO has no website
We require all text in English, this is an English version or blank text areas we can fill in later. OPEN the first 4 files in PHOTOSHOP it represents the 4 different sides of the 2 pieces of paper that will be printed on both sides so 4 designs total.
*YOU CAN USE FAKE TEXT WE CAN FILL IN TEXT LATER* TEXT BOX is Okay. Include; titles,tags, logos, design essentials, text area.etc. detailed text not required

We have uploaded many photos
the map provided can be used
all 4 PhotoShop files can be fixed, redesigned or used
(project started and never finished)
Visit the websites for taglines information, photos etc.

Target Market(s)

International tourists to Okinawa, Japan and American military stationed in Okinawa.

Font styles to use
Serif
Sans Serif

Colors

Designer to choose colors to be used in the design.

Requirements
Must have
• 5 separate businesses and we want each one on a separate page. QRV should be the centerfold 2 page design and we want a cover for "Tidewind Bay Guide" and a map of all the locations on the back......it's 2 pages A4 printed on both sides and folded in half, center stapled to make 4 page pamphlet guide.
• we need
• 1. Cover (highlight Okinawa)
• 2. Back map page
• 3 Tavelo ri hostel page (highlight rooms)
• 4. Bar Lantern page (highlight pool table & darts)
• 5. Vela Bar page (highlight Shi-Sha / HooKah)
• 6. Blue echo page (highlight Karaoke)
• 7. 2 page center spread for QRV Sneakers & Wear
Nice to have
• The Blue echo Karaoke bar can be limited to style, empty text box area etc. we can add information and photos later, please use stock photos to make a working design

```html
<!DOCTYPE html>
<html lang="en">
<head>
<meta charset="utf-8">
<title>Welcome to Tavelori Hostel</title>
<link href="https://fonts.googleapis.com/css2?family=Tinos:wght@400;700&family=Kanit:wght@300&display=swap" rel="stylesheet">
<style>
  :root {
    --backdrop: #e6e6e6;
    --page: #050505;
    --frame: #e4e31c;
    --cyan: #2ec9d6;
    --yellow: #f2ee1a;
    --white: #ffffff;
    --lime: #a8e02a;
    --skyline-deep: #3b3fb8;
    --skyline-mid: #7c86e4;
    --counter-glow: #d9dcf2;
    --shelf-warm: #8a4a2c;
  }
  html, body {
    margin: 0;
    width: 1200px;
    height: 900px;
    overflow: hidden;
    background: var(--backdrop);
  }
  .cover {
    position: absolute;
    left: 303px;
    top: 30px;
    width: 594px;
    height: 840px;
    background: var(--page);
    overflow: hidden;
    box-shadow: 0 6px 24px rgba(0,0,0,.25);
  }
  .cover__frame {
    position: absolute;
    inset: 0;
    z-index: 3;
    pointer-events: none;
  }
  .cover__heading {
    position: absolute;
    left: 0;
    top: 0;
    width: 594px;
    z-index: 4;
  }
  .cover__welcome {
    position: absolute;
    left: 46px;
    top: 116px;
    margin: 0;
    font: 400 42px/1 "Tinos", serif;
    color: var(--white);
    white-space: nowrap;
  }
  .cover__name {
    position: absolute;
    left: 42px;
    top: 166px;
    margin: 0;
    font: 700 80px/1 "Tinos", serif;
    color: var(--cyan);
    letter-spacing: 1px;
    white-space: nowrap;
  }
  .cover__kind {
    position: absolute;
    right: 72px;
    top: 250px;
    margin: 0;
    font: 700 32px/1 "Tinos", serif;
    color: var(--yellow);
    white-space: nowrap;
  }
  .cover__photo {
    position: absolute;
    left: 0;
    top: 292px;
    width: 594px;
    height: 310px;
    z-index: 1;
  }
  .cover__bottles {
    position: absolute;
    right: 22px;
    top: 560px;
    width: 150px;
    height: 130px;
    z-index: 2;
    border-radius: 3px;
    background: linear-gradient(90deg, #2d3a7a 0%, #6b4a2a 30%, #c9897b 60%, #b99a4b 85%, #2a2a2a 100%);
  }
  .brand {
    position: absolute;
    left: 58px;
    top: 690px;
    display: flex;
    align-items: center;
    gap: 14px;
    z-index: 2;
  }
  .brand__mark {
    width: 36px;
    height: 36px;
    border-radius: 50%;
    background: var(--cyan);
  }
  .brand__name {
    font: 300 26px/1 "Kanit", sans-serif;
    color: var(--cyan);
    white-space: nowrap;
  }
  .cover__url {
    position: absolute;
    left: 0;
    right: 0;
    top: 794px;
    margin: 0;
    text-align: center;
    font: 400 17px/1 "Tinos", serif;
    letter-spacing: 7px;
    color: var(--white);
    white-space: nowrap;
  }
</style>
</head>
<body>
  <main class="cover">
    <svg class="cover__frame" width="594" height="840" viewBox="0 0 594 840" aria-hidden="true">
      <polyline points="14,300 14,70 548,70 548,566" fill="none" stroke="var(--frame)" stroke-width="2"/>
      <polyline points="20,690 20,770 574,770" fill="none" stroke="var(--frame)" stroke-width="2"/>
    </svg>

    <header class="cover__heading">
      <p class="cover__welcome">Welcome to</p>
      <h1 class="cover__name">TAVELORI</h1>
      <p class="cover__kind">HOSTEL</p>
    </header>

    <svg class="cover__photo" viewBox="0 0 594 310" role="img" aria-label="Hostel bar counter glowing in blue light, with a city skyline mural behind shelves of bottles">
      <defs>
        <linearGradient id="barScene" x1="0" y1="0" x2="0" y2="1">
          <stop offset="0" stop-color="var(--skyline-deep)"/>
          <stop offset="0.35" stop-color="var(--skyline-mid)"/>
          <stop offset="0.6" stop-color="var(--shelf-warm)"/>
          <stop offset="0.78" stop-color="var(--counter-glow)"/>
          <stop offset="1" stop-color="#3a3a55"/>
        </linearGradient>
        <radialGradient id="barWarmth" cx="0.45" cy="0.6" r="0.5">
          <stop offset="0" stop-color="#e8a36a" stop-opacity="0.45"/>
          <stop offset="1" stop-color="#e8a36a" stop-opacity="0"/>
        </radialGradient>
      </defs>
      <polygon points="0,40 594,0 594,200 0,300" fill="url(#barScene)"/>
      <polygon points="0,40 594,0 594,200 0,300" fill="url(#barWarmth)"/>
      <polyline points="0,300 526,262 594,196" fill="none" stroke="var(--lime)" stroke-width="7"/>
    </svg>

    <div class="cover__bottles" role="img" aria-label="Bottles of local awamori spirits with glasses"></div>

    <div class="brand">
      <span class="brand__mark"></span>
      <span class="brand__name">Tavelo ri hostel</span>
    </div>

    <p class="cover__url">www.tavelostayinn.com</p>
  </main>
</body>
</html>
```